Logo+Business Card Design for Architecture Photographer

Hi Everyone,

I am looking for logo/business designs for my new business - Brovald Studio. My business does commercial photography with a specialization in architecture, luxury real estate, and design. The Int is short for interior and ex is short for exterior.

Some of the values of my business are:
- providing top quality photography and post-processing (straight lines, accurate and bold whites/blacks/colors) for commercial use (websites, social media, advertising campaigns)
- fostering a collaborative workflow that is professional and fun that will have clients returning because of the premium service they received
- asking the right questions so that I can capture what matters to my clients with my own creative vision

I want my final look to be modern and bold. The business cards will be letter pressed/debossed, so the design should incorporate that. I am imagining a solid matte olive green or matte navy blue background on one side and white on the other. The card will be printed on colored cards, so you don't have to put a colored background as part of the design. I have attached some examples of colors I like, although it doesn't matter too much for the purpose of your work.

I want the debossing to be part of the design of the business card. This debossing should be some some of pattern or a frame that holds the logo on the back of the card (I have attached some sample images named geometric debossing to show what I mean). Then I can just foil print my logo on the back. My contact info and a logo will be on the front.

Somewhere it should say "Architecture, Luxury Real Estate, Design".

My vision for the logo: no cameras or buildings. I can't think of anything symbolic for the logo, but it should somehow contain Brovald. It might be cool to have them separated by a line like Bro | Vald. Or have the Int inside something, and the Ex outside.

I plan on using Quelmark to print the cards. You can find their specifications here: https://quelmark.example/products/duplex-business-cards?variant=4837201956372

It would be nice to have a psd file that I can edit as well as a PDF to deliver to the printing company. Both must be vector graphics.

Thank you to everyone who has submitted a design as it has helped me get a better idea of what I want.

Target Market(s)

Designers, architects

Industry/Entity Type

Photographer

Contact Information for Business Card

See project description

Logo Text

Brovald Studio

Font styles to use
Sans Serif
Decorative

Colors
ffffff

Requirements
Must have
• Logo and business card design. Deboss area less than 3 square inches. Deboss area should be some sort of a pattern/design as shown in attachments labelled "Geometric Debossing Example".
• Logo design and deboss design must be submitted in vector graphics.
Nice to have
• Color doesn't have to be shown on the design because I will be printing on colored paper, although it would be helpful to help me visualize what it will eventually look like.
Should not have
• A camera or building in the design...too cliche.

```html
<!DOCTYPE html>
<html lang="en">
<head>
<meta charset="utf-8">
<title>Brovald Studio – Business Card</title>
<link rel="stylesheet" href="https://fonts.googleapis.com/css2?family=Jost:wght@400;500;600;700&display=swap">
<style>
  :root {
    --stage: #2b2d31;
    --card-white: #ffffff;
    --ink: #1f1f1f;
    --ink-soft: #3a3a3a;
    --logo-grey: #4a4a4a;
    --rule: #8a8a8a;
    --navy-top: #3c659f;
    --navy-bottom: #4a79b6;
    --foil: #e6e8ec;
    --tagline: #f4f6fa;
  }
  * { box-sizing: border-box; margin: 0; padding: 0; }
  html, body {
    width: 1200px;
    height: 900px;
    overflow: hidden;
    background: var(--stage);
    font-family: "Jost", sans-serif;
  }
  .canvas {
    position: relative;
    width: 1200px;
    height: 900px;
  }

  /* Front side – white, portrait */
  .card-front {
    position: absolute;
    left: 170px;
    top: 250px;
    width: 320px;
    height: 560px;
    background: var(--card-white);
    border-radius: 4px;
    box-shadow: 0 18px 40px rgba(0,0,0,0.35);
    display: flex;
    flex-direction: column;
    align-items: center;
  }
  .front-logo {
    margin-top: 130px;
    display: flex;
    align-items: center;
    gap: 10px;
    color: var(--logo-grey);
    font-weight: 700;
    font-size: 30px;
    letter-spacing: 0.02em;
  }
  .logo-mark {
    width: 14px;
    height: 14px;
    background: currentColor;
  }
  .front-rule {
    margin-top: 42px;
    width: 240px;
    height: 2px;
    background: linear-gradient(90deg, transparent, var(--rule) 20%, var(--rule) 80%, transparent);
  }
  .contact {
    margin-top: 70px;
    text-align: center;
    color: var(--ink);
  }
  .contact-name {
    font-weight: 600;
    font-size: 19px;
    letter-spacing: 0.12em;
  }
  .contact-role {
    margin-top: 4px;
    font-size: 15px;
    letter-spacing: 0.14em;
    color: var(--ink-soft);
  }
  .contact-line {
    margin-top: 4px;
    font-size: 13px;
    letter-spacing: 0.1em;
    color: var(--ink-soft);
  }
  .contact-role + .contact-line { margin-top: 12px; }

  /* Back side – navy, landscape */
  .card-back {
    position: absolute;
    left: 560px;
    top: 170px;
    width: 560px;
    height: 320px;
    border-radius: 4px;
    overflow: hidden;
    box-shadow: 0 18px 40px rgba(0,0,0,0.35);
  }
  .deboss-pattern {
    position: absolute;
    inset: 0;
    background: linear-gradient(160deg, var(--navy-top), var(--navy-bottom));
  }
  .back-content {
    position: relative;
    height: 100%;
    display: flex;
    flex-direction: column;
    align-items: center;
    justify-content: center;
  }
  .back-logo {
    display: flex;
    align-items: center;
    gap: 12px;
    color: var(--foil);
    font-weight: 700;
    font-size: 40px;
    letter-spacing: 0.02em;
  }
  .back-logo .logo-mark {
    width: 16px;
    height: 16px;
  }
  .tagline {
    margin-top: 16px;
    color: var(--tagline);
    font-size: 15px;
    letter-spacing: 0.08em;
  }
</style>
</head>
<body>
<main class="canvas">

  <section class="card-front" aria-label="Business card front">
    <div class="front-logo">
      <span class="logo-mark" aria-hidden="true"></span>
      <span class="logo-name">Brovald Studio</span>
    </div>
    <div class="front-rule" aria-hidden="true"></div>
    <div class="contact">
      <p class="contact-name">John Doe</p>
      <p class="contact-role">Founder</p>
      <p class="contact-line">+11 44 484 4526</p>
      <p class="contact-line">email@website.com</p>
    </div>
  </section>

  <section class="card-back" aria-label="Business card back">
    <div class="deboss-pattern" role="img" aria-label="Debossed geometric line pattern across the navy card"></div>
    <div class="back-content">
      <div class="back-logo">
        <span class="logo-mark" aria-hidden="true"></span>
        <span class="logo-name">Brovald Studio</span>
      </div>
      <p class="tagline">Architecture, Luxury Real Estate, Design</p>
    </div>
  </section>

</main>
</body>
</html>
```